International Supplier needs an eye catching profssional letterhead and continuation page

We need a letterhead and continuation sheet designed for a company based in Austria called VELMA Screens GmbH. We develop and install innovate glass partition wall solutions to commercial and cultural buildings and to some of the most contemporary architectural buildings in Europe. I have our inhouse design brief confirming our corporate colours, fonts and images and have our corporate logo available in a variety of formats including AI and EPS. We are open to differing design suggestions as long as they follow the colour and font specification in our corporate design brief. We are at the forefront of innovation, craftmanship and design for architectural glass, framing systems and fire rated partition systems. The final design should communicate the spirit and strength of the company.
www.velma.com / www.tarnovu.co.uk / www.brandpane.com

Target Market(s)

Architects, planners, designers, building contractors and construction companies

Industry/Entity Type

Architecture

Font styles to use
Sans Serif

Requirements
Must have
• VELMA Screens GmbH
• Lindorfergasse 4 B
• 7000 Eisenstadt
• Österreich
• Tel: +43 (1) 482 6170
• E-mail:office@velmascreens.at
• Web:www.velmascreens.at / www.velmabrandpane.com
• subtle yet professionally distinctive
• colours and fonts to be taken ffom VELMA design guide but we are also open to variations on the same theme
Should not have
• No bold lines

```html
<!DOCTYPE html>
<html lang="de">
<head>
<meta charset="utf-8">
<title>VELMA Screens GmbH – Letterhead</title>
<link href="https://fonts.googleapis.com/css2?family=Lato:wght@400;700&display=swap" rel="stylesheet">
<style>
  :root{
    --backdrop:#dedede;
    --paper:#f3f3f3;
    --ink-dark:#3a3a3a;
    --ink:#4f4f4f;
    --ink-body:#6c6c6c;
    --accent:#c4214c;
    --rule:#444;
  }
  *{margin:0;padding:0;box-sizing:border-box}
  html,body{width:1163px;height:1200px;overflow:hidden;background:var(--backdrop);font-family:'Lato',sans-serif}
  .letterhead{position:absolute;left:157px;top:0;width:849px;height:1200px;background:var(--paper)}
  .abs{position:absolute}
  .brand{left:100px;top:104px;display:flex;align-items:center;gap:10px}
  .brand-square{width:40px;height:40px;background:var(--accent)}
  .brand-name{font-size:50px;font-weight:400;color:var(--ink-dark);line-height:1;letter-spacing:1px}
  .header-rule{left:346px;top:130px;width:454px;height:2px;background:var(--rule)}
  .address{right:49px;top:110px;font-size:14px;color:var(--ink)}
  .contact{right:49px;font-size:10.5px;color:var(--ink-body);display:flex;align-items:center;gap:6px}
  .contact.phone{top:143px}
  .contact.fax{top:164px}
  .contact svg{width:11px;height:11px;fill:var(--accent)}
  .recipient{left:98px;top:297px;color:var(--ink)}
  .recipient .salutation{font-size:14.5px;font-weight:700}
  .recipient .designation{font-size:9.5px;margin-top:-2px}
  .recipient .company{font-size:14.5px;font-weight:700;margin-top:-1px}
  .date{right:61px;top:297px;font-size:14.5px;font-weight:700;color:var(--ink)}
  .body-text{left:98px;width:702px;font-size:13.9px;line-height:17.3px;color:var(--ink-body);text-align:justify}
  .body-text.emphasis{font-weight:700;color:var(--ink)}
  .signature{left:98px;top:938px;width:136px;height:32px}
  .signature-mark{width:100%;height:28px;background:linear-gradient(90deg,#d9d9d9,#cfcfcf)}
  .signature-rule{width:100%;height:1px;background:var(--rule);margin-top:2px}
  .signer{left:99px;top:991px}
  .signer .name{font-size:17.5px;font-weight:700;color:var(--accent);letter-spacing:1px}
  .signer .role{font-size:13px;color:var(--ink);margin-top:1px}
  .footer-line{left:97px;top:1123px;width:629px;height:2px;background:var(--rule)}
  .footer-item{left:97px;font-size:10px;color:var(--ink-body);display:flex;align-items:center;gap:14px}
  .footer-item.mail{top:1104px}
  .footer-item.web{top:1131px}
  .footer-item svg{width:14px;height:12px}
  .footer-square{left:744px;top:1096px;width:52px;height:52px;background:var(--accent)}
</style>
</head>
<body>
<div class="letterhead">
  <div class="abs brand">
    <div class="brand-square"></div>
    <div class="brand-name">VELMA</div>
  </div>
  <div class="abs header-rule"></div>
  <div class="abs address">Lindorfergasse 4 B 7000 Eisenstadt Österreich</div>
  <div class="abs contact phone">
    <svg viewBox="0 0 24 24"><path d="M6.6 10.8a15 15 0 0 0 6.6 6.6l2.2-2.2c.3-.3.7-.4 1-.2 1.1.4 2.3.6 3.6.6.6 0 1 .4 1 1V20c0 .6-.4 1-1 1A17 17 0 0 1 3 4c0-.6.4-1 1-1h3.5c.6 0 1 .4 1 1 0 1.3.2 2.5.6 3.6.1.3 0 .7-.2 1z"/></svg>
    +43 (1) 482 6170
  </div>
  <div class="abs contact fax">
    <svg viewBox="0 0 24 24"><path d="M6 2h12v5H6zM3 8h18v9h-3v5H6v-5H3zm5 7v5h8v-5z"/></svg>
    +07 5182 6304
  </div>

  <div class="abs recipient">
    <div class="salutation">Dear, Mr________</div>
    <div class="designation">Designation</div>
    <div class="company">Company Name</div>
  </div>
  <div class="abs date">DATE:08/02/2018</div>

  <p class="abs body-text" style="top:400px">Lorem Ipsum is simply dummy text of the printing and typesetting industry. Lorem Ipsum has been the industry's standard dummy text ever since the1500s,when an unknown printer took a galley of type and scrambled it to make a type specimen book. It has survived not only five centuries, but also the leap into electronic typesetting, remaining essentially unchanged. It was popularised in the 1960s with the release of Letraset sheets containing Lorem Ipsum passages,and more recently with desktop publishing software like Aldus PageMaker including versions of Lorem Ipsum.</p>
  <p class="abs body-text" style="top:514px">Lorem Ipsum is simply dummy text of the printing and typesetting industry. Lorem Ipsum has been the industry's standard dummy text ever since the1500s,when an unknown printer took a galley of type and scrambled it to make a type specimen book. It has survived not only five centuries, but also the leap into electronic typesetting, remaining essentially unchanged. It was popularised in the 1960s with the release of Letraset sheets containing Lorem Ipsum passages,and more recently with desktop publishing software like Aldus PageMaker including versions of Lorem Ipsum.</p>
  <p class="abs body-text emphasis" style="top:639px">Lorem Ipsum is simply dummy text of the printing and typesetting industry. Lorem Ipsum has been the industry's standard dummy text ever since the1500s,when an unknown printer took a galley of type and scrambled it to make a type specimen book.</p>
  <p class="abs body-text" style="top:704px">Lorem Ipsum is simply dummy text of the printing and typesetting industry. Lorem Ipsum has been the industry's standard dummy text ever since the1500s,when an unknown printer took a galley of type and scrambled it to make a type specimen book. It has survived not only five centuries, but also the leap into electronic typesetting, remaining essentially unchanged. It was popularised in the 1960s with the release of Letraset sheets containing Lorem Ipsum passages,and more recently with desktop publishing software like Aldus PageMaker including versions of Lorem Ipsum.</p>
  <p class="abs body-text" style="top:825px">Lorem Ipsum is simply dummy text of the printing and typesetting industry. Lorem Ipsum has been the industry's standard dummy text ever since the1500s,when an unknown printer took a galley of type and scrambled it to make a type specimen book.</p>

  <div class="abs signature">
    <div class="signature-mark" role="img" aria-label="Handwritten signature"></div>
    <div class="signature-rule"></div>
  </div>
  <div class="abs signer">
    <div class="name">YOUR NAME</div>
    <div class="role">Designation</div>
  </div>

  <div class="abs footer-item mail">
    <svg viewBox="0 0 14 12"><rect x="0.5" y="1" width="13" height="10" fill="var(--accent)"/><path d="M0.5 1.5 7 7l6.5-5.5M0.5 11 5.5 6M13.5 11 8.5 6" stroke="#fff" stroke-width="1" fill="none"/></svg>
    office@velmascreens.at
  </div>
  <div class="abs footer-line"></div>
  <div class="abs footer-item web">
    <svg viewBox="0 0 14 14"><circle cx="7" cy="7" r="6" fill="none" stroke="var(--accent)" stroke-width="1.3"/><ellipse cx="7" cy="7" rx="2.6" ry="6" fill="none" stroke="var(--accent)" stroke-width="1"/><path d="M1 7h12M2 4h10M2 10h10" stroke="var(--accent)" stroke-width="0.9"/></svg>
    www.velmascreens.at / www.velmabrandpane.com
  </div>
  <div class="abs footer-square"></div>
</div>
</body>
</html>
```